Birchfield Dental Care Stationery

create stationery, business cards and envelops for business. Use current logo on website but open to new fonts for the business name. Business name is Birchfield Dental Care, would like below the name added "Cosmetic - Family - Implants" Website is www.birchfielddentalcareQX.example. I would like to have modern look, clean, and professional. The water mark of the logo is a great thing to ad as well.

Target Market(s)

General public, Families, Cosmetic, Implant

Industry/Entity Type

Dental

Font styles to use
Sans Serif

Colors
9bcb3c
000000
757575
c9c9c9

Requirements
Must have
• Would like to see different versions of the current logo. Improvements, color, sytle, and class.
Nice to have
• current font has double "oo" in the Birchfield logo, does not need to have with new logo.

```html
<!DOCTYPE html>
<html lang="en">
<head>
<meta charset="utf-8">
<title>Birchfield Dental Care – Business Cards</title>
<link href="https://fonts.googleapis.com/css2?family=Montserrat:wght@500;600;700;800&display=swap" rel="stylesheet">
<style>
  :root {
    --backdrop: #6b4a2c;
    --blue-light: #3a8fd6;
    --blue: #1f6fc6;
    --blue-deep: #1658b0;
    --slate-dark: #1f2530;
    --slate: #3a414c;
    --green: #9bcb3c;
    --white: #ffffff;
    --shadow: rgba(0, 0, 0, 0.45);
  }
  * { margin: 0; padding: 0; box-sizing: border-box; }
  html, body {
    width: 1200px;
    height: 1000px;
    overflow: hidden;
    background: var(--backdrop);
    font-family: "Montserrat", Arial, sans-serif;
  }
  .canvas {
    position: relative;
    width: 1200px;
    height: 1000px;
  }
  .card {
    position: absolute;
    width: 700px;
    height: 400px;
    overflow: hidden;
    box-shadow: 0 14px 30px var(--shadow);
  }

  /* ---- Back card (blue) ---- */
  .card--back {
    left: 110px;
    top: 70px;
    background: linear-gradient(110deg, var(--blue-deep) 0%, var(--blue) 50%, var(--blue-light) 100%);
  }
  .brand {
    position: absolute;
    display: flex;
    align-items: center;
    gap: 18px;
  }
  .brand__mark {
    width: 76px;
    height: 76px;
    border-radius: 50%;
    border: 5px solid var(--green);
    flex: none;
  }
  .brand__name {
    font-weight: 800;
    font-size: 26px;
    line-height: 0.95;
    text-transform: uppercase;
    letter-spacing: 0.5px;
  }
  .brand__tagline {
    margin-top: 5px;
    font-weight: 600;
    font-size: 11.5px;
    letter-spacing: 0.2px;
  }
  .card--back .brand { left: 220px; top: 120px; }
  .card--back .brand__name,
  .card--back .brand__tagline { color: var(--green); }

  .watermark {
    position: absolute;
    border-radius: 50%;
    border: 4px solid rgba(255, 255, 255, 0.12);
    background: rgba(255, 255, 255, 0.05);
  }
  .card--back .watermark { width: 170px; height: 170px; left: 500px; top: 90px; }

  .website {
    position: absolute;
    left: 0;
    right: 0;
    bottom: 70px;
    text-align: center;
    color: var(--white);
    font-weight: 700;
    font-size: 20px;
    letter-spacing: 0.3px;
  }

  /* ---- Front card (dark) ---- */
  .card--front {
    left: 390px;
    top: 520px;
    background: linear-gradient(100deg, var(--slate-dark) 0%, var(--slate-dark) 40%, var(--slate) 100%);
  }
  .card--front .brand { left: 200px; top: 90px; }
  .card--front .brand__name,
  .card--front .brand__tagline { color: var(--white); }
  .card--front .watermark { width: 150px; height: 150px; left: 560px; top: 150px; border-color: rgba(31, 111, 198, 0.18); background: rgba(31, 111, 198, 0.08); }

  .contact {
    position: absolute;
    left: 230px;
    top: 220px;
    display: flex;
    align-items: stretch;
    gap: 22px;
    color: var(--green);
  }
  .contact__person {
    text-align: right;
    font-weight: 700;
    font-size: 19px;
    line-height: 1.15;
    padding-top: 28px;
  }
  .contact__divider {
    width: 2px;
    background: var(--green);
  }
  .contact__details {
    list-style: none;
    font-weight: 600;
    font-size: 18px;
    line-height: 1.2;
  }

  .band {
    position: absolute;
    left: 0;
  }
  .band--accent-blue { left: 72%; right: 0; top: 300px; height: 40px; background: var(--blue); }
  .band--green { width: 72%; top: 340px; height: 24px; background: var(--green); }
  .band--blue { right: 0; top: 364px; height: 14px; background: var(--blue-deep); }
</style>
</head>
<body>
<main class="canvas">

  <section class="card card--back" aria-label="Business card back">
    <div class="watermark" aria-hidden="true"></div>
    <div class="brand">
      <span class="brand__mark" aria-hidden="true"></span>
      <div>
        <p class="brand__name">Birchfield<br>Dental Care</p>
        <p class="brand__tagline">Cosmetic • Family • Implants</p>
      </div>
    </div>
    <p class="website">www.birchfielddentalcareQX.example</p>
  </section>

  <section class="card card--front" aria-label="Business card front">
    <div class="watermark" aria-hidden="true"></div>
    <div class="brand">
      <span class="brand__mark" aria-hidden="true"></span>
      <div>
        <p class="brand__name">Birchfield<br>Dental Care</p>
        <p class="brand__tagline">Cosmetic • Family • Implants</p>
      </div>
    </div>
    <div class="contact">
      <p class="contact__person">Your Name<br>Position</p>
      <span class="contact__divider" aria-hidden="true"></span>
      <ul class="contact__details">
        <li>name@email.com</li>
        <li>000.000.0000</li>
        <li>000.000.0000</li>
      </ul>
    </div>
    <div class="band band--accent-blue" aria-hidden="true"></div>
    <div class="band band--green" aria-hidden="true"></div>
    <div class="band band--blue" aria-hidden="true"></div>
  </section>

</main>
</body>
</html>
```